New homepage design - Cobalt Sages

- we would like to have a new website layout of the existing one: www.cobaltsages.ch
the new layout should have the following parameters:
- we want it to be minimalistic
- clear lines
- not too colourful (eventually also more in grey tone?)

our company: cobalt sages
- cobalt sages is an organizational consulting company and we work with organizations and individuals alike
- we are headquartered in the engadine
- examples: www.pelmartine.nyc, www.trodwickandhale.com, www.femorasix.com, www.daryluntley.website,

Target Market(s)

Companies

Industry/Entity Type

Consulting

Number of Pages Required

1 page

Font styles to use
Sans Serif

Colors

Designer to choose only greyscale colors for use in the design.

Requirements
Must have
• A minimalistic design
Nice to have
• minimalistic and slick
Should not have
• not too many colours

```html
<!DOCTYPE html>
<html lang="en">
<head>
<meta charset="utf-8">
<title>Cobalt Sages – Turn Growth into Thriving</title>
<link href="https://fonts.googleapis.com/css2?family=Roboto:wght@300;400;500;700&display=swap" rel="stylesheet">
<style>
:root{
  --ink:#2a2a2a;
  --ink-mid:#444;
  --accent:#333;
  --line-soft:#bdbdbd;
  --frame:#d9d9d9;
  --text:#5a5a5a;
  --text-light:#6e6e6e;
  --bg-top:#e6e6e6;
  --bg-pale:#f5f5f5;
  --panel:#c4c4c4;
  --white:#fff;
  --footer:#2b2b2b;
}
*{margin:0;padding:0;box-sizing:border-box}
html,body{width:1200px;height:3784px;overflow:hidden}
body{
  position:relative;font-family:'Roboto',sans-serif;color:var(--text);
  background:linear-gradient(180deg,var(--bg-top) 0,#ededed 500px,var(--bg-pale) 900px,#f3f3f3 1600px,#eeeeee 2200px,var(--bg-pale) 2900px,#f2f2f2 3417px);
}
.abs{position:absolute}
.center{left:0;width:1200px;text-align:center}
.top-rule{top:0;left:0;width:1200px;height:3px;background:var(--ink)}
.hero-glow{top:0;left:0;width:1200px;height:680px;
  background:radial-gradient(ellipse 700px 300px at 250px 420px,rgba(200,200,200,.55),transparent),radial-gradient(ellipse 600px 260px at 950px 200px,rgba(215,215,215,.5),transparent)}
.brand-mark{width:46px;height:46px;border:2px solid var(--ink);border-radius:50%;left:577px}
.brand-name{font-weight:300;color:var(--ink-mid);letter-spacing:1px}
.brand-tag{font-weight:400;letter-spacing:2.5px;color:#666}
.nav a{position:absolute;font-size:13px;color:#222;text-decoration:none;font-weight:400}
.hero-title{top:300px;font-size:70px;font-weight:300;color:var(--ink);letter-spacing:1px}
.hero-sub{top:396px;font-size:50px;font-weight:300;color:#444;letter-spacing:1px}
.btn-outline{left:511px;top:473px;width:178px;height:60px;border:1.5px solid var(--ink-mid);border-radius:30px;
  font-size:18px;color:var(--ink);display:flex;align-items:center;justify-content:center}
.intro-title{top:620px;font-size:48px;font-weight:400;color:var(--ink)}
.intro{top:698px}
.intro p{font-size:13px;line-height:27px;color:var(--text);width:760px;margin:0 auto 28px;font-weight:300}
.frame{border:1px solid var(--frame);border-radius:16px}
.panel{border-radius:14px;background:linear-gradient(180deg,#cfcfcf,#bdbdbd)}
.sec-head{font-weight:300;color:var(--ink)}
.rule{height:3px;background:var(--ink)}
.why-text p{font-size:13px;line-height:24.7px;text-align:justify;font-weight:300;margin-bottom:24px;color:var(--text)}
.card{background:var(--white);border:1px solid #ececec;border-radius:6px;box-shadow:0 2px 6px rgba(0,0,0,.04);text-align:center}
.card .logo{position:absolute;top:52px;left:0;width:100%;font-size:40px;font-weight:500;color:var(--ink-mid)}
.card .quote{position:absolute;top:136px;left:28px;right:28px;font-size:13px;line-height:25.7px;font-weight:300;color:var(--text)}
.card .name{position:absolute;top:310px;left:0;width:100%;font-size:18px;font-weight:500;color:var(--ink)}
.card .role{position:absolute;top:342px;left:0;width:100%;font-size:11px;color:#555}
.feature h3{font-size:32px;font-weight:300;color:#555;text-align:center}
.feature p{font-size:13px;line-height:25px;color:var(--text-light);text-align:center;font-weight:300;margin:14px auto 0;width:410px}
.btn-solid{width:141px;height:49px;background:var(--ink);color:var(--white);font-size:16px;display:flex;align-items:center;justify-content:center}
.footer{top:3417px;left:0;width:1200px;height:367px;background:var(--footer);color:var(--white)}
.footer .brand-mark{border-color:var(--white);top:18px}
.footer .nav a{color:var(--white)}
.social{width:36px;height:36px;border:1.5px solid var(--white);border-radius:50%}
.copy{font-size:16px;font-weight:400}
</style>
</head>
<body>
<div class="abs top-rule"></div>
<div class="abs hero-glow"></div>

<header>
  <div class="abs brand-mark" style="top:16px"></div>
  <div class="abs center brand-name" style="top:98px;font-size:30px">COBALT SAGES</div>
  <div class="abs center brand-tag" style="top:134px;font-size:12px">TURN GROWTH INTO THRIVING</div>
  <nav class="nav">
    <a class="abs" style="left:213px;top:176px">COBALT SAGES</a>
    <a class="abs" style="left:363px;top:176px">COBALT SAGES</a>
    <a class="abs" style="left:513px;top:176px">EXECUTIVE CIRCLE</a>
    <a class="abs" style="left:689px;top:176px">FOR CORPORATIONS</a>
    <a class="abs" style="left:877px;top:176px">FOR INDIVIDUALS</a>
  </nav>
</header>

<section class="hero">
  <h1 class="abs center hero-title">COBALT SAGES</h1>
  <div class="abs center hero-sub">TURN GROWTH INTO THRIVING</div>
  <div class="abs btn-outline">LEARN MORE</div>
</section>

<section class="intro-block">
  <h2 class="abs center intro-title">COBALT SAGES</h2>
  <div class="abs center intro">
    <p>We convert the speak of purpose and consciousness into solutions. We are deeply convinced that a life and work ethics based on the attitude of serving all stakeholders and developing high levels of inclusiveness, gratitude and consciousness would lead to more happiness and superior results for all.</p>
    <p>Our own purpose is to focus on these topics for the benefit of companies and leaders alike, thus creating an increased level of self-awareness, responsibility, fairness and alignment.</p>
    <p>Seeing leaders and companies intensely passionate for what they engage in and achieving results beyond what has been thought possible fills us with joy and gives us great fulfilment.</p>
  </div>
</section>

<section class="why">
  <div class="abs" role="img" aria-label="Alpine valley with village and mountains" style="left:0;top:999px;width:511px;height:543px;background:linear-gradient(180deg,#dcdcdc 0,#a9a9a9 25%,#7a7a7a 50%,#8e8e8e 72%,#5c5c5c 100%)"></div>
  <div class="abs frame" style="left:344px;top:1083px;width:320px;height:374px"></div>
  <div class="abs panel" role="img" aria-label="Dandelion bud on a soft plain background" style="left:358px;top:1094px;width:294px;height:353px"></div>
  <h2 class="abs sec-head" style="left:712px;top:1034px;font-size:36px">WHY WE DO IT</h2>
  <div class="abs" style="left:712px;top:1089px;width:66px;height:2px;background:var(--line-soft)"></div>
  <div class="abs why-text" style="left:712px;top:1124px;width:371px">
    <p>The “Cobalt Sages-Retreats” embrace a holistic approach. The number of participants is limited to a maximum of 12 leaders per retreat in order to guarantee intimacy and intensity. Target participants are C-Level executives, senior corporate managers, entrepreneurs, politicians, artists and sports people. In short: people who resume responsibility, are role-models for others, want to initiate and move things, create sustainable value and commit to following their highest consciousness at all times. Nevertheless, throughout the retreat we focus on the human being rather than the role and function.</p>
    <p>The magic of the group lies in the personality, context, intentions and experiences of the participants themselves. Therefore, participation is upon invitation only. If you are interested, please contact Matthias or Leonie for more information and obtaining your personal invitation.</p>
  </div>
</section>

<section class="retreats">
  <h2 class="abs center sec-head" style="top:1634px;font-size:44px">RETREATS IN PONTRESINA</h2>
  <div class="abs rule" style="left:569px;top:1700px;width:62px"></div>
  <svg class="abs" style="left:0;top:1741px" width="1200" height="437" viewBox="0 0 1200 437">
    <defs>
      <linearGradient id="lakeA" x1="0" y1="0" x2="0" y2="1"><stop offset="0" stop-color="#e0e0e0"/><stop offset=".4" stop-color="#8a8a8a"/><stop offset=".6" stop-color="#9c9c9c"/><stop offset="1" stop-color="#5e5e5e"/></linearGradient>
      <linearGradient id="lakeB" x1="0" y1="0" x2="0" y2="1"><stop offset="0" stop-color="#c8c8c8"/><stop offset=".4" stop-color="#8f8f8f"/><stop offset=".7" stop-color="#b4b4b4"/><stop offset="1" stop-color="#cfcfcf"/></linearGradient>
      <linearGradient id="road" x1="0" y1="0" x2="0" y2="1"><stop offset="0" stop-color="#a5a5a5"/><stop offset=".45" stop-color="#e2e2e2"/><stop offset=".6" stop-color="#8d8d8d"/><stop offset="1" stop-color="#616161"/></linearGradient>
    </defs>
    <path role="img" aria-label="Mountain lake with forested slopes" d="M0 60 L350 0 Q358 0 358 8 L358 429 Q358 437 350 437 L0 376 Z" fill="url(#lakeA)"/>
    <rect role="img" aria-label="Alpine lake with pebble shore" x="378" y="0" width="446" height="437" rx="8" fill="url(#lakeB)"/>
    <path role="img" aria-label="Mountain pass road under open sky" d="M845 8 Q845 0 853 1 L1200 70 L1200 378 L853 436 Q845 437 845 429 Z" fill="url(#road)"/>
  </svg>
</section>

<section class="testimonials">
  <h2 class="abs center sec-head" style="top:2244px;font-size:44px">TESTIMONIALS</h2>
  <div class="abs rule" style="left:569px;top:2310px;width:62px"></div>

  <div class="abs card" style="left:112px;top:2340px;width:308px;height:401px">
    <div class="logo">meridale</div>
    <div class="quote">A truly exceptional network of professionals from very different backgrounds who share similar values and beliefs – and, often enough, similar experiences and challenges – even though they have never met before. Exciting and enriching.</div>
    <div class="name">Henrik Vallmer</div>
    <div class="role">Chief Financial Officer, Meridale</div>
  </div>
  <div class="abs card" style="left:445px;top:2340px;width:310px;height:401px">
    <div class="logo" style="font-weight:400">corvanta</div>
    <div class="quote" style="left:40px;right:40px">The retreat was an open and warm exchange between special individuals who follow their own ways that don’t necessarily correspond to standard career paths.</div>
    <div class="name">Dr. Marta L. Oberlin</div>
    <div class="role">CEO Corvanta AG, Board Member HALVEX – Corvanta AG</div>
  </div>
  <div class="abs card" style="left:779px;top:2340px;width:309px;height:401px">
    <div class="logo" style="font-size:32px;top:58px;font-weight:400">brightlane</div>
    <div class="quote" style="left:36px;right:36px">The Cobalt Sages team enabled me to discuss current and relevant topics in a safe setting, with the group acting as sparring partner and supporter to find solutions.</div>
    <div class="name">Lukas Brenndorf</div>
    <div class="role">COO, Brightlane Systems</div>
  </div>
</section>

<section class="features">
  <div class="abs" role="img" aria-label="Silhouette of a climber against a sunset sky" style="left:112px;top:2806px;width:470px;height:319px;border-radius:8px;background:linear-gradient(180deg,#5a5a5a 0,#a8a8a8 45%,#bdbdbd 60%,#2a2a2a 100%)"></div>
  <div class="abs" role="img" aria-label="Hands clapping with a cloud of chalk dust" style="left:618px;top:2806px;width:470px;height:319px;border-radius:8px;background:radial-gradient(ellipse at 50% 45%,#bdbdbd,#3a3a3a 70%,#1e1e1e)"></div>

  <div class="abs feature" style="left:112px;top:3150px;width:470px">
    <h3>WHY WE DO IT</h3>
    <p>Seeing leaders and companies intensely passionate for what they engage in and achieving results beyond what has been thought possible fills us with joy and gives us great fulfilment.</p>
  </div>
  <div class="abs feature" style="left:618px;top:3150px;width:470px">
    <h3>HOW WE DO IT</h3>
    <p>We convert the speak of purpose and consciousness into concrete solutions. We offer our services to corporations and individuals and a special series of retreats to the wider public.</p>
  </div>
  <div class="abs btn-solid" style="left:277px;top:3302px">READ MORE</div>
  <div class="abs btn-solid" style="left:785px;top:3302px">READ MORE</div>
</section>

<footer class="abs footer">
  <div class="abs brand-mark"></div>
  <div class="abs center" style="top:98px;font-size:38px;font-weight:300;letter-spacing:1px">COBALT SAGES</div>
  <div class="abs center" style="top:142px;font-size:14px;letter-spacing:3px">TURN GROWTH INTO THRIVING</div>
  <nav class="nav">
    <a class="abs" style="left:213px;top:187px">COBALT SAGES</a>
    <a class="abs" style="left:363px;top:187px">COBALT SAGES</a>
    <a class="abs" style="left:513px;top:187px">EXECUTIVE CIRCLE</a>
    <a class="abs" style="left:689px;top:187px">FOR CORPORATIONS</a>
    <a class="abs" style="left:877px;top:187px">FOR INDIVIDUALS</a>
  </nav>
  <div class="abs social" style="left:496px;top:236px" aria-label="Social link"></div>
  <div class="abs social" style="left:539px;top:236px" aria-label="Social link"></div>
  <div class="abs social" style="left:581px;top:236px" aria-label="Social link"></div>
  <div class="abs social" style="left:624px;top:236px" aria-label="Social link"></div>
  <div class="abs social" style="left:667px;top:236px" aria-label="Social link"></div>
  <div class="abs center copy" style="top:303px">© Copyright 2022 Cobalt Sages.All Rights Reserved</div>
</footer>
</body>
</html>
```